International Tour Operator Needs A New Brochure

We are a newly set up small tour operator focusing on personal tailor made honeymoons for our guests.

We would like to see our logo incorporated into the brochure design as well as our website: mirabelfenwickjourneys.co.uk; our e-mail address tobias@mirabelfenwickjourneys.co.uk; and our mobile number +44 (0)7812469035.

Where as the logo is required, the content in the word document does not have to be used/included. It is there to provide background information on what we do.

The final design should be professional, clear/not crowded, attention grabbing and fit the industry and target segment (brides and grooms).

Target Market(s)

Brides and grooms

Industry/Entity Type

Industry

Colors

Designer to choose colors to be used in the design.

Requirements
Must have
• Logo
Nice to have
• Some content from the word document

```html
<!DOCTYPE html>
<html lang="en">
<head>
<meta charset="utf-8">
<title>South East Asia – Honeymoon Destinations</title>
<link href="https://fonts.googleapis.com/css2?family=Great+Vibes&family=Questrial&family=Muli:wght@700&display=swap" rel="stylesheet">
<style>
  :root {
    --cream: #f8efdc;
    --card: #ffffff;
    --sage: #bcd0c5;
    --ribbon-edge: #7d6b65;
    --script-green: #3f6b57;
    --body-grey: #6d6d6d;
    --heading-green: #4b5d56;
    --label: #ffffff;
  }
  html, body {
    margin: 0;
    padding: 0;
    overflow: hidden;
  }
  .page {
    position: relative;
    width: 840px;
    height: 1200px;
    background: var(--cream);
    overflow: hidden;
    font-family: "Questrial", "Century Gothic", sans-serif;
  }
  .intro-card {
    position: absolute;
    left: 38px;
    top: 230px;
    width: 761px;
    height: 364px;
    background: var(--card);
    box-shadow: 0 3px 8px rgba(0,0,0,0.28);
    text-align: center;
  }
  .intro-text {
    position: absolute;
    left: 40px;
    right: 40px;
    top: 103px;
    margin: 0;
    font-size: 16.5px;
    line-height: 24px;
    color: var(--body-grey);
  }
  .destinations {
    position: absolute;
    left: 0;
    right: 0;
    top: 250px;
    color: var(--heading-green);
    font-size: 16.5px;
    line-height: 20px;
  }
  .destinations h2 {
    margin: 0 0 2px;
    font-family: "Muli", "Century Gothic", sans-serif;
    font-weight: 700;
    font-size: 16.5px;
  }
  .destinations ul {
    list-style: none;
    margin: 0;
    padding: 0;
    color: var(--body-grey);
  }
  .title-ribbon {
    position: absolute;
    left: 265px;
    top: 0;
    width: 305px;
    height: 310px;
    filter: drop-shadow(2px 4px 4px rgba(0,0,0,0.3));
  }
  .title-ribbon h1 {
    position: absolute;
    left: 0;
    right: 0;
    top: 30px;
    margin: 0;
    text-align: center;
    font-family: "Great Vibes", cursive;
    font-weight: 400;
    font-size: 62px;
    line-height: 88px;
    color: var(--script-green);
  }
  .title-ribbon h1 span { display: block; }
  .photo-panel {
    position: absolute;
    left: 38px;
    width: 761px;
    filter: drop-shadow(0 2px 4px rgba(0,0,0,0.25));
  }
  .photo-panel svg { display: block; }
  .photo-label {
    position: absolute;
    right: 20px;
    top: 8px;
    font-family: "Muli", sans-serif;
    font-weight: 700;
    font-size: 17px;
    color: var(--label);
  }
  .panel-maldives { top: 620px; height: 262px; }
  .panel-thailand { top: 907px; height: 265px; }
</style>
</head>
<body>
<div class="page">

  <section class="intro-card">
    <p class="intro-text">Friendly people, beautiful beaches and a rich cultural heritage awaits you in Asia. If you are willing to spend two days in transit Asia Is a great venue. You are sure to enjoy the delights that the Orient has to offer if you like amazing beaches, exploring new cultures and getting pampered.</p>
    <div class="destinations">
      <h2>Key destinations</h2>
      <ul>
        <li>Maldives</li>
        <li>Thailand</li>
        <li>Bali</li>
        <li>Sri Lanka</li>
      </ul>
    </div>
  </section>

  <header class="title-ribbon">
    <svg width="305" height="310" viewBox="0 0 305 310">
      <polygon points="0,0 305,0 305,307 152.5,228 0,307" fill="var(--sage)" stroke="var(--ribbon-edge)" stroke-width="3"/>
      <polyline points="11,0 11,289 152.5,216 294,289 294,0" fill="none" stroke="var(--ribbon-edge)" stroke-width="1.5" stroke-dasharray="6 4"/>
    </svg>
    <h1><span>South East</span><span>Asia</span></h1>
  </header>

  <figure class="photo-panel panel-maldives" style="margin:0">
    <svg width="761" height="262" viewBox="0 0 761 262" role="img" aria-label="Photo of a Maldives resort: thatched overwater villa and palm tree beside a turquoise infinity pool opening onto the sea under a blue sky">
      <defs>
        <linearGradient id="maldivesTones" x1="0" y1="0" x2="0" y2="1">
          <stop offset="0" stop-color="#2f63b8"/>
          <stop offset="0.45" stop-color="#9cc4e4"/>
          <stop offset="0.55" stop-color="#2a8fb0"/>
          <stop offset="1" stop-color="#6fd6d8"/>
        </linearGradient>
      </defs>
      <path d="M13,0 H748 A13,13 0 0 0 761,13 V249 A13,13 0 0 0 748,262 H13 A13,13 0 0 0 0,249 V13 A13,13 0 0 0 13,0 Z" fill="url(#maldivesTones)"/>
    </svg>
    <figcaption class="photo-label">Maldives</figcaption>
  </figure>

  <figure class="photo-panel panel-thailand" style="margin:0">
    <svg width="761" height="265" viewBox="0 0 761 265" role="img" aria-label="Photo of a Thai royal palace with golden spired roofs, white walls and sculpted topiary trees on a lawn">
      <defs>
        <linearGradient id="thailandTones" x1="0" y1="0" x2="0" y2="1">
          <stop offset="0" stop-color="#8fb3d8"/>
          <stop offset="0.35" stop-color="#d9e4ee"/>
          <stop offset="0.55" stop-color="#c9a25a"/>
          <stop offset="0.8" stop-color="#e9e6df"/>
          <stop offset="1" stop-color="#5f8a3e"/>
        </linearGradient>
      </defs>
      <path d="M13,0 H748 A13,13 0 0 0 761,13 V252 A13,13 0 0 0 748,265 H13 A13,13 0 0 0 0,252 V13 A13,13 0 0 0 13,0 Z" fill="url(#thailandTones)"/>
    </svg>
    <figcaption class="photo-label">Thailand</figcaption>
  </figure>

</div>
</body>
</html>
```